Letterhead & Business Card Design Project

Use existing logo to create a new letterhead and business card design. Looking for something clean modern using color options of black, white and gray. The green from the logo may be used lightly as an accent color.

Target Market(s)

Professional business people

Industry/Entity Type

Business

Requirements
Must have
• Business card with front and back design using existing logo.
Nice to have
• Professional presentation
Clean look
Should not have
• No oil rigs, pumpjacks or clip art.

```html
<!DOCTYPE html>
<html lang="en">
<head>
<meta charset="utf-8">
<title>Halden Exploration – Business Card</title>
<link href="https://fonts.googleapis.com/css2?family=Source+Sans+3:wght@400&display=swap" rel="stylesheet">
<style>
  :root {
    --sheet: #dcdddf;
    --card: #ffffff;
    --ink: #111111;
    --band: #050505;
    --band-back: #231f20;
    --accent: #3db34a;
    --muted: #5a5a5a;
    --label: #ffffff;
    --crop: #111111;
  }
  * { margin: 0; padding: 0; box-sizing: border-box; }
  html, body {
    width: 960px; height: 1200px; overflow: hidden;
    background: var(--sheet);
    font-family: "Source Sans 3", "Myriad Pro", Arial, sans-serif;
  }
  .sheet { position: relative; width: 960px; height: 1200px; }
  .crop-marks { position: absolute; inset: 0; }
  .crop-marks line { stroke: var(--crop); stroke-width: 1.2; }

  .card {
    position: absolute; left: 90px; width: 760px; height: 424px;
    background: var(--card); overflow: hidden;
  }
  .card--front { top: 88px; }
  .card--back { top: 667px; }

  .front-wordmark {
    position: absolute; left: 0; right: 0; top: 228px;
    text-align: center; font-size: 40px; letter-spacing: 7px;
    color: var(--ink); font-weight: 400;
  }
  .front-rule {
    position: absolute; left: 0; right: 0; top: 374px; height: 2px;
    background: var(--accent);
  }
  .front-band {
    position: absolute; left: 0; right: 0; top: 376px; bottom: 0;
    background: var(--band);
  }

  .contact {
    position: absolute; left: 30px; top: 20px;
    font-size: 22px; line-height: 29px; color: var(--ink);
  }
  .contact p + p { margin-top: 29px; }
  .back-wordmark {
    position: absolute; left: 30px; top: 232px;
    font-size: 20px; letter-spacing: 3px; color: var(--ink); font-weight: 400;
  }
  .website {
    position: absolute; left: 30px; top: 322px;
    font-size: 21px; color: var(--muted);
  }
  .back-band {
    position: absolute; left: 0; right: 0; top: 373px; bottom: 0;
    background: var(--band-back);
  }
  .back-band__accent {
    position: absolute; left: 0; top: 0; bottom: 0; width: 28px;
    background: var(--accent);
  }

  .side-label {
    position: absolute; left: 103px;
    font-size: 32px; color: var(--label); line-height: 1;
  }
  .side-label--front { top: 520px; }
  .side-label--back { top: 1095px; }
</style>
</head>
<body>
<main class="sheet">
  <svg class="crop-marks" width="960" height="1200" viewBox="0 0 960 1200" aria-hidden="true">
    <!-- front card -->
    <line x1="90" y1="44" x2="90" y2="88"/><line x1="43" y1="88" x2="90" y2="88"/>
    <line x1="850" y1="44" x2="850" y2="88"/><line x1="850" y1="88" x2="898" y2="88"/>
    <line x1="90" y1="512" x2="90" y2="560"/><line x1="43" y1="512" x2="90" y2="512"/>
    <line x1="850" y1="512" x2="850" y2="560"/><line x1="850" y1="512" x2="898" y2="512"/>
    <!-- back card -->
    <line x1="90" y1="621" x2="90" y2="667"/><line x1="43" y1="667" x2="90" y2="667"/>
    <line x1="850" y1="621" x2="850" y2="667"/><line x1="850" y1="667" x2="898" y2="667"/>
    <line x1="90" y1="1090" x2="90" y2="1136"/><line x1="43" y1="1090" x2="90" y2="1090"/>
    <line x1="850" y1="1090" x2="850" y2="1136"/><line x1="850" y1="1090" x2="898" y2="1090"/>
  </svg>

  <section class="card card--front" aria-label="Card front">
    <div class="front-wordmark">HALDEN EXPLORATION</div>
    <div class="front-rule"></div>
    <div class="front-band"></div>
  </section>
  <div class="side-label side-label--front">front design</div>

  <section class="card card--back" aria-label="Card back">
    <div class="contact">
      <p>Halden Exploration<br>4520 North Cedar Ave<br>Suite 310<br>Brookfield, OK 74120</p>
      <p>Phone 918.555.0142<br>Fax 918.555.0143</p>
    </div>
    <div class="back-wordmark">HALDEN EXPLORATION</div>
    <div class="website">www.haldenexploration.com</div>
    <div class="back-band"><div class="back-band__accent"></div></div>
  </section>
  <div class="side-label side-label--back">back design</div>
</main>
</body>
</html>
```